Customer Dashboard Design for Email Security SaaS

Mailvornet is a commercial email spam filter offered as a SaaS product, built and operated by a small German hosting provider. It protects business email accounts against spam, phishing, scam, and viruses using a multilayer filtering pipeline that combines traditional spam detection with AI-powered classification. The product runs entirely on German infrastructure, ensuring data sovereignty for European customers.

We need a complete redesign of the customer-facing dashboard. This is the web application where paying customers manage their email filtering: view their mail log, check quarantined emails, manage allow/blocklists, configure their settings, and handle their subscription. It is the primary touchpoint between Mailvornet and its customers.

Our customers are system administrators, IT managers at small-to-medium businesses, and operators of small hosting providers. They are technically competent but not designers. They expect professional, efficient tools that respect their time. They typically manage 10–500 email accounts and check the dashboard a few times per week, with heavier use during spam incidents.

We have attached the current mockups which really need to be replaced with something good looking.

Target Market(s)

System administrators, IT managers at small-to-medium businesses, and operators of small hosting providers.

Industry/Entity Type

SaaS

Number of Pages Required

5+ page

```html
<!DOCTYPE html>
<html lang="en">
<head>
<meta charset="utf-8">
<title>Mailvornet – Dashboard</title>
<link href="https://fonts.googleapis.com/css2?family=Manrope:wght@400;500;600;700;800&family=Space+Mono:wght@700&display=swap" rel="stylesheet">
<style>
:root{
  --bg:#000;
  --sidebar:#0a0a0a;
  --line:#262626;
  --card:#080808;
  --card-border:#2c2c2c;
  --green:#12a56b;
  --green-bright:#1fbf7d;
  --green-dark:#0b3a26;
  --text:#f4f4f4;
  --muted:#b9b9b9;
  --dim:#8a8a8a;
  --chip:#1c1c1c;
  --orange:#e8872a;
  --red:#e2544f;
  --pink:#f06a8a;
  --blue:#3aa0e8;
}
*{box-sizing:border-box;margin:0;padding:0}
html,body{width:1200px;height:967px;overflow:hidden;background:var(--bg);color:var(--text);font-family:"Manrope",sans-serif}
.app{position:relative;width:1200px;height:967px}

.sidebar{position:absolute;left:0;top:0;width:243px;height:967px;background:var(--sidebar);border-right:1px solid var(--line)}
.brand{position:absolute;left:35px;top:31px;display:flex;align-items:center;gap:13px}
.brand-mark{width:41px;height:41px;border-radius:10px;background:var(--green)}
.brand-name{font-size:22px;font-weight:700;color:var(--text)}
.nav{position:absolute;left:9px;top:102px;width:222px;list-style:none}
.nav-item{height:41px;margin-bottom:4px;display:flex;align-items:center;padding-left:42px;gap:16px;font-size:16.5px;color:var(--text);border-radius:4px}
.nav-item svg{width:18px;height:18px;stroke:#8c8c8c;fill:none;stroke-width:1.6;stroke-linecap:round;stroke-linejoin:round}
.nav-item.active{background:#0f5236;border-left:3px solid var(--green-bright);padding-left:39px}
.nav-item.active svg{stroke:#fff}
.user{position:absolute;left:0;top:892px;width:243px;height:75px;border-top:1px solid var(--line);display:flex;align-items:center;padding-left:24px}
.avatar{width:37px;height:37px;border-radius:50%;background:var(--green);display:flex;align-items:center;justify-content:center;font-size:13px;font-weight:500}
.user-info{margin-left:9px;line-height:1.15}
.user-name{font-size:13px;font-weight:800}
.user-mail{font-size:10.5px;color:var(--muted)}
.user-caret{position:absolute;right:22px;top:32px;width:10px;height:10px;stroke:#aaa;fill:none;stroke-width:1.6}

.main{position:absolute;left:308px;top:0;width:830px}
.greeting{position:absolute;top:54px;left:0;font-size:27px;font-weight:800;letter-spacing:-.3px}
.greeting-sub{position:absolute;top:84px;left:0;font-size:17px;color:#ddd;font-weight:400}
.date{position:absolute;left:697px;top:60px;width:133px;height:36px;border:1px solid var(--line);border-radius:4px;background:#0b0b0b;font-size:11.5px;display:flex;align-items:center;justify-content:center}

.total{position:absolute;top:148px;left:0;width:830px;height:123px;border:1px solid #0f4a31;border-top:4px solid var(--green);border-radius:6px;background:linear-gradient(90deg,#000 65%,#0b2e20 100%)}
.total-label{position:absolute;left:49px;top:24px;font-size:13px;color:var(--green-bright);font-weight:500}
.total-value{position:absolute;left:49px;top:36px;font-family:"Space Mono",monospace;font-size:42px;font-weight:700}
.total-sub{position:absolute;left:50px;top:86px;font-size:13px;color:#ccc}

.stats{position:absolute;top:284px;left:0;display:flex;gap:9px}
.stat{position:relative;width:159px;height:161px;border:1px solid var(--card-border);border-radius:8px;background:var(--card)}
.stat-icon{position:absolute;left:20px;top:17px;width:36px;height:36px;border-radius:7px;display:flex;align-items:center;justify-content:center}
.stat-icon svg{width:22px;height:22px;fill:none;stroke-width:1.8;stroke-linecap:round;stroke-linejoin:round}
.trend{position:absolute;right:12px;top:27px;font-size:9.5px;color:#ddd;display:flex;align-items:center;gap:2px}
.trend svg{width:7px;height:7px;stroke:var(--green-bright);fill:none;stroke-width:1.6}
.stat-value{position:absolute;left:18px;top:64px;font-family:"Space Mono",monospace;font-size:23px;font-weight:700}
.stat-label{position:absolute;left:17px;top:92px;font-size:12.5px;color:#ddd}
.stat-sub{position:absolute;left:18px;top:108px;font-size:10.5px;color:var(--muted)}
.stat-link{position:absolute;left:18px;top:129px;font-size:6.5px;color:var(--green-bright);display:flex;align-items:center;gap:3px}
.stat-link svg{width:8px;height:8px;stroke:var(--green-bright);fill:none;stroke-width:1.6}

.activity{position:absolute;top:462px;left:0;width:830px;height:330px;border:1px solid #0f4a31;border-radius:8px;background:var(--bg)}
.activity-title{position:absolute;left:38px;top:24px;font-size:22px;font-weight:800}
.activity-sub{position:absolute;left:38px;top:51px;font-size:11px;color:#ccc}
.filters{position:absolute;left:38px;top:77px;display:flex;gap:5px}
.chip{height:21px;padding:0 16px;border-radius:11px;background:var(--chip);font-size:9px;display:flex;align-items:center}
.chip.on{background:var(--green);padding:0 21px}
.range{position:absolute;left:697px;top:54px;height:21px;border-radius:11px;background:#1a1a1a;display:flex;align-items:center;padding:2px;font-size:8.5px}
.range span{padding:0 8px;height:17px;display:flex;align-items:center;border-radius:9px}
.range .on{background:#000}
.chart{position:absolute;left:41px;top:117px;width:748px;height:177px;background:#0b0b0b}
.chart svg{display:block}
.axis{font-family:"Manrope",sans-serif;font-size:8px;fill:#8a8a8a}

.qa-title{position:absolute;top:814px;left:0;font-size:17.5px;color:#bcbcbc;font-weight:500}
.qa{position:absolute;top:861px;width:396px;height:80px;border-radius:8px;display:flex;align-items:center;padding-left:24px}
.qa-green{left:0;border:1px solid #0f4a31}
.qa-grey{left:421px;border:1px solid var(--card-border);background:#0b0b0b}
.qa-icon{width:50px;height:50px;border-radius:8px}
.qa-green .qa-icon{background:#0a2019}
.qa-grey .qa-icon{background:#1e1e1e}
.qa-text{margin-left:15px;line-height:1.3}
.qa-name{font-size:13px;font-weight:800}
.qa-green .qa-name{color:var(--green-bright)}
.qa-desc{font-size:10.5px;color:#c4c4c4}
</style>
</head>
<body>
<div class="app">
  <aside class="sidebar">
    <div class="brand"><div class="brand-mark"></div><span class="brand-name">Mailvornet</span></div>
    <ul class="nav">
      <li class="nav-item active"><svg viewBox="0 0 24 24"><rect x="3" y="3" width="7" height="9" rx="1"/><rect x="14" y="3" width="7" height="5" rx="1"/><rect x="14" y="12" width="7" height="9" rx="1"/><rect x="3" y="16" width="7" height="5" rx="1"/></svg>Dashboard</li>
      <li class="nav-item"><svg viewBox="0 0 24 24"><path d="M8 21h12a2 2 0 0 0 2-2v-2H10v2a2 2 0 1 1-4 0V5a2 2 0 0 0-2-2H3a2 2 0 0 0-1 2v2h4"/><path d="M19 17V5a2 2 0 0 0-2-2H4"/><path d="M10 8h6M10 12h6"/></svg>Mail Log</li>
      <li class="nav-item"><svg viewBox="0 0 24 24"><rect x="3" y="3" width="18" height="5" rx="1"/><path d="M5 8v11a2 2 0 0 0 2 2h10a2 2 0 0 0 2-2V8M10 12h4"/></svg>Quarantine</li>
      <li class="nav-item"><svg viewBox="0 0 24 24"><path d="M22 12h-6l-2 3h-4l-2-3H2"/><path d="M5.5 5h13L22 12v6a2 2 0 0 1-2 2H4a2 2 0 0 1-2-2v-6z"/></svg>Mailboxes</li>
      <li class="nav-item"><svg viewBox="0 0 24 24"><path d="M12 22s8-4 8-10V5l-8-3-8 3v7c0 6 8 10 8 10z"/></svg>Allowlist</li>
      <li class="nav-item"><svg viewBox="0 0 24 24"><circle cx="12" cy="12" r="10"/><path d="M5 5l14 14"/></svg>Blocklist</li>
      <li class="nav-item"><svg viewBox="0 0 24 24"><circle cx="12" cy="12" r="3"/><path d="M19.4 15a1.7 1.7 0 0 0 .3 1.8l.1.1a2 2 0 1 1-2.8 2.8l-.1-.1a1.7 1.7 0 0 0-2.8 1.2V21a2 2 0 1 1-4 0v-.1a1.7 1.7 0 0 0-2.8-1.2l-.1.1a2 2 0 1 1-2.8-2.8l.1-.1A1.7 1.7 0 0 0 3 14.1H3a2 2 0 1 1 0-4h.1a1.7 1.7 0 0 0 1.2-2.8l-.1-.1a2 2 0 1 1 2.8-2.8l.1.1a1.7 1.7 0 0 0 2.8-1.2V3a2 2 0 1 1 4 0v.1a1.7 1.7 0 0 0 2.8 1.2l.1-.1a2 2 0 1 1 2.8 2.8l-.1.1a1.7 1.7 0 0 0 1.2 2.8H21a2 2 0 1 1 0 4h-.1a1.7 1.7 0 0 0-1.5.9z"/></svg>Settings</li>
      <li class="nav-item"><svg viewBox="0 0 24 24"><rect x="2" y="5" width="20" height="14" rx="2"/><path d="M2 10h20"/></svg>Billing</li>
    </ul>
    <div class="user">
      <div class="avatar">JB</div>
      <div class="user-info"><div class="user-name">Jonas Berger</div><div class="user-mail">j.berger@netzwerkhaus-...</div></div>
      <svg class="user-caret" viewBox="0 0 10 10"><path d="M1 3l4 4 4-4"/></svg>
    </div>
  </aside>

  <main class="main">
    <h1 class="greeting">Good afternoon, Jonas.</h1>
    <p class="greeting-sub">Here's your email security overview.</p>
    <div class="date">Tuesday, 14 April 2026</div>

    <section class="total">
      <div class="total-label">TOTAL EMAILS FILTERED</div>
      <div class="total-value">8,247</div>
      <div class="total-sub">across all mailboxes, all time</div>
    </section>

    <section class="stats">
      <div class="stat">
        <div class="stat-icon" style="background:#3a2212"><svg viewBox="0 0 24 24" stroke="#e8872a"><path d="M19.7 14a6.9 6.9 0 0 0 .3-2V5l-8-3-3.2 1.2M4.7 4.7 4 5v7c0 6 8 10 8 10a20.3 20.3 0 0 0 5.6-4.4M2 2l20 20"/></svg></div>
        <div class="trend"><svg viewBox="0 0 8 8"><path d="M1 7l6-6M2 1h5v5"/></svg>12%</div>
        <div class="stat-value">2,134</div><div class="stat-label">Spam Blocked</div><div class="stat-sub">Last 30 days</div>
      </div>
      <div class="stat">
        <div class="stat-icon" style="background:#3a1616"><svg viewBox="0 0 24 24" stroke="#e2544f"><path d="M10.3 3.9 1.8 18a2 2 0 0 0 1.7 3h17a2 2 0 0 0 1.7-3L13.7 3.9a2 2 0 0 0-3.4 0zM12 9v4M12 17h.01"/></svg></div>
        <div class="trend"><svg viewBox="0 0 8 8"><path d="M1 7l6-6M2 1h5v5"/></svg>5%</div>
        <div class="stat-value">387</div><div class="stat-label">Phishing Detected</div><div class="stat-sub">Last 30 days</div>
      </div>
      <div class="stat">
        <div class="stat-icon" style="background:#3a1622"><svg viewBox="0 0 24 24" stroke="#f06a8a"><path d="M8 2l1.9 1.9M16 2l-1.9 1.9M9 7.1V6a3 3 0 1 1 6 0v1.1"/><path d="M12 20c-3.3 0-6-2.7-6-6v-3a4 4 0 0 1 4-4h4a4 4 0 0 1 4 4v3c0 3.3-2.7 6-6 6zM12 20v-9M6.5 9C4.6 8.8 3 7.1 3 5M6 13H2M3 21c0-2.1 1.7-3.9 3.8-4M20.97 5c0 2.1-1.6 3.8-3.5 4M22 13h-4M17.2 17c2.1.1 3.8 1.9 3.8 4"/></svg></div>
        <div class="trend"><svg viewBox="0 0 8 8"><path d="M1 1l6 6M7 2v5H2"/></svg>8%</div>
        <div class="stat-value">43</div><div class="stat-label">Viruses Caught</div><div class="stat-sub">Last 30 days</div>
      </div>
      <div class="stat">
        <div class="stat-icon" style="background:#12283a"><svg viewBox="0 0 24 24" stroke="#3aa0e8"><rect x="2" y="4" width="20" height="16" rx="2"/><path d="m22 7-10 6L2 7"/></svg></div>
        <div class="trend"><svg viewBox="0 0 8 8"><path d="M1 1l6 6M7 2v5H2"/></svg>3%</div>
        <div class="stat-value">1,209</div><div class="stat-label">Newsletters Sorted</div><div class="stat-sub">Last 30 days</div>
      </div>
      <div class="stat">
        <div class="stat-icon" style="background:#3a1e10"><svg viewBox="0 0 24 24" stroke="#f07a2a"><path d="M12 22s8-4 8-10V5l-8-3-8 3v7c0 6 8 10 8 10zM12 8v4M12 16h.01"/></svg></div>
        <div class="trend"><svg viewBox="0 0 8 8"><path d="M1 7l6-6M2 1h5v5"/></svg>2%</div>
        <div class="stat-value">12</div><div class="stat-label">In Quarantine</div><div class="stat-sub">Awaiting review</div>
        <div class="stat-link">View quarantine<svg viewBox="0 0 8 8"><path d="M1 4h6M4 1l3 3-3 3"/></svg></div>
      </div>
    </section>

    <section class="activity">
      <h2 class="activity-title">Email Activity</h2>
      <p class="activity-sub">Filtered volume over time</p>
      <div class="range"><span>7 days</span><span class="on">30 days</span></div>
      <div class="filters">
        <span class="chip on">All</span><span class="chip">Spam</span><span class="chip">Phishing</span><span class="chip">Newsletter</span><span class="chip">Virus</span>
      </div>
      <div class="chart">
        <svg width="748" height="177" viewBox="0 0 748 177" role="img" aria-label="Filtered email volume per day, Mar 16 to Apr 13">
          <defs>
            <linearGradient id="spamFill" x1="0" y1="0" x2="0" y2="1"><stop offset="0" stop-color="#e8872a" stop-opacity=".3"/><stop offset="1" stop-color="#e8872a" stop-opacity=".05"/></linearGradient>
            <linearGradient id="newsFill" x1="0" y1="0" x2="0" y2="1"><stop offset="0" stop-color="#8a9ab0" stop-opacity=".25"/><stop offset="1" stop-color="#8a9ab0" stop-opacity=".03"/></linearGradient>
            <linearGradient id="phishFill" x1="0" y1="0" x2="0" y2="1"><stop offset="0" stop-color="#e2544f" stop-opacity=".3"/><stop offset="1" stop-color="#e2544f" stop-opacity=".05"/></linearGradient>
          </defs>
          <g stroke="#333" stroke-dasharray="3 3" stroke-width=".6">
            <line x1="23" y1="10" x2="739" y2="10"/><line x1="23" y1="45" x2="739" y2="45"/><line x1="23" y1="79" x2="739" y2="79"/><line x1="23" y1="114" x2="739" y2="114"/><line x1="23" y1="148" x2="739" y2="148"/>
          </g>
          <g class="axis" text-anchor="end">
            <text x="18" y="13">120</text><text x="18" y="48">90</text><text x="18" y="83">60</text><text x="18" y="118">30</text><text x="18" y="152">0</text>
          </g>
          <g class="axis" text-anchor="middle">
            <text x="24" y="160">Mar 16</text><text x="147" y="160">Mar 21</text><text x="271" y="160">Mar 26</text><text x="395" y="160">Mar 31</text><text x="518" y="160">Apr 05</text><text x="642" y="160">Apr 10</text>
          </g>
          <path fill="url(#spamFill)" d="M23 25C35 25 35 8 47 8C61 8 61 27 75 27C86 27 86 28 97 28C111 28 111 11 125 11C136 11 136 78 147 78C160 78 160 75 172 75C185 75 185 45 197 45C222 45 222 70 247 70C260 70 260 25 272 25C284 25 284 53 295 53C308 53 308 22 320 22C331 22 331 75 342 75C356 75 356 70 370 70C383 70 383 92 395 92C408 92 408 19 420 19C431 19 431 53 442 53C455 53 455 8 467 8C485 8 485 19 503 19C512 19 512 31 520 31C532 31 532 12 543 12C560 12 560 14 576 14C585 14 585 25 593 25C606 25 606 92 618 92C631 92 631 72 643 72C657 72 657 70 671 70C682 70 682 53 693 53C704 53 704 32 715 32C727 32 727 95 739 95L739 148L23 148Z"/>
          <path fill="none" stroke="#e8872a" stroke-width="1.2" d="M23 25C35 25 35 8 47 8C61 8 61 27 75 27C86 27 86 28 97 28C111 28 111 11 125 11C136 11 136 78 147 78C160 78 160 75 172 75C185 75 185 45 197 45C222 45 222 70 247 70C260 70 260 25 272 25C284 25 284 53 295 53C308 53 308 22 320 22C331 22 331 75 342 75C356 75 356 70 370 70C383 70 383 92 395 92C408 92 408 19 420 19C431 19 431 53 442 53C455 53 455 8 467 8C485 8 485 19 503 19C512 19 512 31 520 31C532 31 532 12 543 12C560 12 560 14 576 14C585 14 585 25 593 25C606 25 606 92 618 92C631 92 631 72 643 72C657 72 657 70 671 70C682 70 682 53 693 53C704 53 704 32 715 32C727 32 727 95 739 95"/>
          <path fill="url(#newsFill)" d="M23 111C35 111 35 56 47 56C60 56 60 106 72 106C85 106 85 70 97 70C110 70 110 109 122 109C135 109 135 73 147 73C160 73 160 103 172 103C185 103 185 56 197 56C208 56 208 100 219 100C231 100 231 103 242 103C253 103 253 120 264 120C278 120 278 109 292 109C306 109 306 67 320 67C333 67 333 120 345 120C358 120 358 70 370 70C383 70 383 117 395 117C407 117 407 59 419 59C431 59 431 120 442 120C455 120 455 73 467 73C480 73 480 117 492 117C505 117 505 75 517 75C530 75 530 84 543 84C554 84 554 95 565 95C579 95 579 120 593 120C606 120 606 120 618 120C631 120 631 67 643 67C657 67 657 95 671 95C682 95 682 120 693 120C704 120 704 97 715 97C727 97 727 64 739 64L739 148L23 148Z"/>
          <path fill="none" stroke="#4a7bc0" stroke-width="1.2" d="M23 111C35 111 35 56 47 56C60 56 60 106 72 106C85 106 85 70 97 70C110 70 110 109 122 109C135 109 135 73 147 73C160 73 160 103 172 103C185 103 185 56 197 56C208 56 208 100 219 100C231 100 231 103 242 103C253 103 253 120 264 120C278 120 278 109 292 109C306 109 306 67 320 67C333 67 333 120 345 120C358 120 358 70 370 70C383 70 383 117 395 117C407 117 407 59 419 59C431 59 431 120 442 120C455 120 455 73 467 73C480 73 480 117 492 117C505 117 505 75 517 75C530 75 530 84 543 84C554 84 554 95 565 95C579 95 579 120 593 120C606 120 606 120 618 120C631 120 631 67 643 67C657 67 657 95 671 95C682 95 682 120 693 120C704 120 704 97 715 97C727 97 727 64 739 64"/>
          <path fill="url(#phishFill)" stroke="#d9564a" stroke-width="1.1" d="M23 134C35 134 35 127 47 127C61 127 61 128 75 128C86 128 86 142 97 142C111 142 111 128 125 128C136 128 136 139 147 139C160 139 160 139 172 139C196 139 196 127 219 127C233 127 233 127 247 127C260 127 260 139 272 139C285 139 285 125 297 125C309 125 309 120 320 120C333 120 333 139 345 139C358 139 358 122 370 122C383 122 383 131 395 131C408 131 408 124 420 124C431 124 431 131 442 131C465 131 465 127 487 127C502 127 502 134 517 134C541 134 541 134 565 134C579 134 579 124 593 124C606 124 606 136 618 136C645 136 645 124 671 124C682 124 682 142 693 142C716 142 716 135 739 135"/>
          <path fill="none" stroke="#e8405a" stroke-width="1.1" d="M23 144C60 144 80 146 120 145C200 147 260 144 320 146C400 147 450 145 520 146C600 147 650 145 693 146C720 147 730 144 739 143"/>
        </svg>
      </div>
    </section>

    <h2 class="qa-title">Quick Actions</h2>
    <div class="qa qa-green"><div class="qa-icon"></div><div class="qa-text"><div class="qa-name">View Quarantine</div><div class="qa-desc">Release or delete held emails</div></div></div>
    <div class="qa qa-grey"><div class="qa-icon"></div><div class="qa-text"><div class="qa-name">Check Mail Log</div><div class="qa-desc">Browse full filtering history</div></div></div>
  </main>
</div>
</body>
</html>
```